Postcard Design for a book promotion

I have written a book which I want to market, and promo. The postcard is an advertisement for promotional purposes. The book is titled "Iron Over Cloud." By T.J. Marlow. I have a website: http://ironovercloud.info. I can upload graphics, photos or details.

The story is about a Waist Gunner and Crew 274 of the 612th Bomb Squadron who flew and fought over Germany in World War II.

All of the crew survived.

T J Marlow, on Chatterbook and http://ironovercloud. info

Industry/Entity Type

Promo

```html
<!DOCTYPE html>
<html lang="en">
<head>
<meta charset="utf-8">
<title>Iron Over Cloud – Book Promo Postcard</title>
<link rel="stylesheet" href="https://fonts.googleapis.com/css2?family=Parisienne&family=Tinos:wght@400;700&family=Arimo:wght@400;700&family=Open+Sans:wght@800&display=swap">
<style>
  :root {
    --page: #e4e4e2;
    --ink: #0c0c0c;
    --paper: #ffffff;
    --accent: #e2ee1e;
    --text-light: #f2f2f2;
    --muted: #9a9a9a;
    --line: #8c8c8c;
  }
  * { box-sizing: border-box; margin: 0; padding: 0; }
  html, body { width: 1200px; height: 1200px; overflow: hidden; }
  body { background: var(--page); position: relative; font-family: "Arimo", sans-serif; }

  .card { position: absolute; left: 180px; width: 840px; height: 560px; overflow: hidden;
          box-shadow: 0 6px 18px rgba(0,0,0,.25); }
  .card--front { top: 26px; background: var(--ink); }
  .card--back { top: 614px; background: var(--paper); }

  .hero-photo { position: absolute; left: 0; top: 0; width: 100%; height: 330px;
    background: linear-gradient(180deg, #c4c4c4 0%, #9a9a9a 45%, #3a3a3a 82%, var(--ink) 100%); }
  .hero-fade { position: absolute; left: 0; top: 0; width: 100%; height: 330px;
    background: linear-gradient(90deg, rgba(12,12,12,.9) 0%, rgba(12,12,12,.35) 40%, rgba(12,12,12,0) 100%); }
  .band { position: absolute; left: 0; top: 450px; width: 100%; height: 70px;
    background: linear-gradient(180deg, rgba(70,70,70,0) 0%, rgba(70,70,70,.4) 100%); }

  .you { position: absolute; font-family: "Parisienne", cursive; color: var(--text-light); line-height: 1; }
  .tagline { position: absolute; font-family: "Tinos", serif; color: var(--text-light); white-space: nowrap; }
  .title { position: absolute; font-family: "Open Sans", sans-serif; font-weight: 800; color: var(--accent);
           text-transform: uppercase; white-space: nowrap; }

  .front .you { left: 150px; top: 108px; font-size: 56px; }
  .front .tagline { left: 200px; top: 168px; font-size: 21px; }
  .front .title { left: 140px; top: 198px; font-size: 36px; }

  .author-photo--round { position: absolute; left: 105px; top: 268px; width: 126px; height: 126px; border-radius: 50%;
    border: 5px solid #5a5a5a; background: radial-gradient(circle at 50% 60%, #6b5a4e 0%, #4a4a4a 60%, #2a2a2a 100%); }
  .blurb { position: absolute; color: var(--text-light); line-height: 1.35; }
  .front .blurb { left: 250px; top: 290px; width: 350px; font-size: 13px; }
  .author-label { position: absolute; color: var(--text-light); white-space: nowrap; }
  .front .author-label { left: 262px; top: 352px; font-size: 19px; }
  .author-name { position: absolute; color: var(--text-light); font-weight: 700; letter-spacing: 1px; white-space: nowrap; }
  .front .author-name { left: 262px; top: 374px; font-size: 27px; }
  .url { position: absolute; font-family: "Tinos", serif; color: var(--text-light); white-space: nowrap; }
  .front .url { left: 280px; top: 432px; font-size: 18px; }

  .book { position: absolute; background: var(--paper); box-shadow: 4px 4px 8px rgba(0,0,0,.5);
          font-family: "Tinos", serif; color: var(--ink); text-align: center; }
  .book__title { font-size: 17px; margin-top: 10px; white-space: nowrap; }
  .book__image { margin: 8px auto 0; width: 82%; height: 38px;
    background: linear-gradient(180deg, #d8d8d8, #7a7a7a); }
  .book__text { font-size: 6.5px; line-height: 1.3; margin: 8px 10px 0; }
  .book__author { font-size: 10px; margin-top: 8px; }
  .front .book { left: 640px; top: 260px; width: 140px; height: 196px; }

  .promo-panel { position: absolute; left: 0; top: 0; width: 410px; height: 470px; background: var(--ink); }
  .back .you { left: 30px; top: 18px; font-size: 44px; }
  .back .tagline { left: 70px; top: 60px; font-size: 16px; }
  .back .title { left: 30px; top: 82px; font-size: 29px; }
  .back .blurb { left: 32px; top: 134px; width: 345px; font-size: 12px; text-align: justify; }
  .author-photo--square { position: absolute; left: 48px; top: 262px; width: 96px; height: 84px;
    border: 3px solid #d9d9d9; background: linear-gradient(160deg, #8b8f93 0%, #5c4d44 60%, #3a3a3a 100%); }
  .back .author-label { left: 76px; top: 354px; font-size: 12px; }
  .back .author-name--small { position: absolute; left: 60px; top: 370px; font-size: 12px; color: var(--text-light); white-space: nowrap; }
  .back .book { left: 236px; top: 250px; width: 84px; height: 120px; }
  .back .book__title { font-size: 10px; margin-top: 6px; }
  .back .book__image { height: 24px; margin-top: 5px; }
  .back .book__text { font-size: 4px; margin: 5px 6px 0; }
  .back .book__author { font-size: 6px; margin-top: 5px; }
  .back .url { left: 222px; top: 392px; font-size: 12px; }

  .stamp-box { position: absolute; right: 52px; top: 64px; width: 96px; height: 82px; border: 1.5px solid #b0b0b0;
    font-size: 13px; color: var(--muted); text-align: center; line-height: 1.1; padding-top: 17px; }
  .address-line { position: absolute; left: 470px; width: 310px; height: 0; border-top: 1.5px solid var(--line); }
</style>
</head>
<body>

<section class="card card--front front" aria-label="Postcard front">
  <div class="hero-photo" role="img" aria-label="Black and white photo of a four-engine bomber in flight"></div>
  <div class="hero-fade"></div>
  <div class="band"></div>
  <p class="you">YOU</p>
  <p class="tagline">can't afford to Miss EITHER!</p>
  <h1 class="title">“Iron Over Cloud”</h1>
  <div class="author-photo--round" role="img" aria-label="Photo of the author seated in an armchair"></div>
  <p class="blurb">The story is about a Waist Gunner and Crew 274 of the 612th Bomb Squadron who flew and fought over Germany in World War II.</p>
  <p class="author-label">Author</p>
  <p class="author-name">T.J. MARLOW</p>
  <p class="url">http://ironovercloud.info</p>
  <div class="book">
    <p class="book__title">Iron Over Cloud</p>
    <div class="book__image" role="img" aria-label="Photo of a bomber on the book cover"></div>
    <p class="book__text">A story about a waist gunner in the U.S. Army Air Forces who flew over the Reich in a four-engine heavy bomber.</p>
    <p class="book__author">T. J. Marlow</p>
  </div>
</section>

<section class="card card--back back" aria-label="Postcard back">
  <div class="promo-panel">
    <p class="you">YOU</p>
    <p class="tagline">can't afford to Miss EITHER!</p>
    <h2 class="title">“Iron Over Cloud”</h2>
    <p class="blurb">This tribute is about the men who courageously flew and fought in peril, half frozen, suspended in the air five miles above the ground. The men of Crew 274 were more than ordinary men, they were extraordinary men doing an extraordinary job.</p>
    <div class="author-photo--square" role="img" aria-label="Photo of the author seated in an armchair"></div>
    <p class="author-label">Author</p>
    <p class="author-name--small">T.J. MARLOW</p>
    <div class="book">
      <p class="book__title">Iron Over Cloud</p>
      <div class="book__image" role="img" aria-label="Photo of a bomber on the book cover"></div>
      <p class="book__text">A story about a waist gunner in the U.S. Army Air Forces who flew over the Reich in a four-engine heavy bomber.</p>
      <p class="book__author">T. J. Marlow</p>
    </div>
    <p class="url">http://ironovercloud.info</p>
  </div>
  <div class="stamp-box">Place<br>Stamp<br>Here</div>
  <div class="address-line" style="top:300px"></div>
  <div class="address-line" style="top:350px"></div>
  <div class="address-line" style="top:400px"></div>
</section>

</body>
</html>
```